Brightstone Roofing Business Card

This is my current business card. But I’d like to make some changes. Somewhere on the card I’d like to list some of the services we offer. Maybe on the back? But I’d still like to keep the red. White and black modern look.

-residential & commercial roofing
-Roof Repairs & Maintenance
-Storm Damage & Insurance Claims specialist
-Christmas Lights and permanent Christmas lights
Fencing. Windows. Gutters. Siding. Sheetrock, painting.

```html
<!DOCTYPE html>
<html lang="en">
<head>
<meta charset="utf-8">
<title>Brightstone Roofing Business Card</title>
<link rel="stylesheet" href="https://fonts.googleapis.com/css2?family=Michroma&family=Work+Sans:wght@400;500&display=swap">
<style>
  :root {
    --backdrop: #d4d4d4;
    --ink: #0b0b0b;
    --red: #e3262b;
    --red-bright: #f0343a;
    --red-deep: #8c1418;
    --red-dark: #5e0d10;
    --white: #ffffff;
    --grey-text: #d9d9d9;
  }
  * { box-sizing: border-box; margin: 0; padding: 0; }
  html, body { width: 1200px; height: 854px; overflow: hidden; }
  body {
    background: var(--backdrop);
    font-family: "Work Sans", Arial, sans-serif;
    position: relative;
  }
  .card {
    position: absolute;
    top: 272px;
    width: 540px;
    height: 309px;
    border-radius: 24px;
    overflow: hidden;
  }
  .card--front { left: 40px; }
  .card--back { left: 620px; background: var(--ink); }

  /* front */
  .tartan-field {
    position: absolute; inset: 0;
    background:
      radial-gradient(ellipse 40% 35% at 25% 20%, rgba(255,255,255,.35), transparent 70%),
      radial-gradient(ellipse 35% 30% at 80% 55%, rgba(255,255,255,.22), transparent 70%),
      radial-gradient(ellipse 30% 30% at 92% 15%, rgba(11,11,11,.55), transparent 70%),
      radial-gradient(ellipse 30% 35% at 85% 90%, rgba(11,11,11,.45), transparent 70%),
      radial-gradient(ellipse 30% 30% at 10% 70%, rgba(11,11,11,.35), transparent 70%),
      radial-gradient(ellipse 55% 50% at 40% 35%, var(--red-bright), transparent 75%),
      linear-gradient(160deg, var(--red) 0%, var(--red-deep) 45%, var(--red) 70%, var(--red-dark) 100%);
  }
  .front-brand {
    position: absolute; inset: 0;
    display: flex; align-items: center; justify-content: center; gap: 18px;
  }
  .brand-dot {
    width: 74px; height: 74px; border-radius: 50%;
    background: var(--red); border: 4px solid var(--ink);
    flex: none;
  }
  .brand-name {
    font-family: "Michroma", "Work Sans", sans-serif;
    font-size: 30px; line-height: 1.2;
    color: var(--white);
    letter-spacing: 1px;
  }

  /* back */
  .back-brand {
    position: absolute; top: 26px; left: 0; right: 0;
    display: flex; align-items: center; justify-content: center; gap: 12px;
  }
  .back-brand .brand-dot { width: 46px; height: 46px; border-width: 3px; }
  .back-brand .brand-name { font-size: 17px; color: var(--red); }
  .contact-row {
    position: absolute; top: 112px; left: 0; right: 0;
    display: flex; justify-content: center; align-items: stretch;
  }
  .person { text-align: right; padding-right: 18px; }
  .person-name {
    font-family: "Michroma", "Work Sans", sans-serif;
    font-size: 20px; color: var(--white); letter-spacing: 2px;
  }
  .person-name .accent { color: var(--red); }
  .person-role { font-size: 14px; color: var(--red); letter-spacing: 1px; margin-top: 2px; }
  .divider { width: 2px; background: var(--red); }
  .contact-list { list-style: none; padding-left: 16px; }
  .contact-list li {
    display: flex; align-items: center; gap: 10px;
    font-size: 14px; color: var(--grey-text); line-height: 24px; letter-spacing: .5px;
  }
  .contact-list svg { width: 12px; height: 12px; fill: var(--red); flex: none; }
  .services {
    position: absolute; top: 208px; left: 0; right: 0;
    display: flex; justify-content: center;
  }
  .services-col {
    list-style: none; padding: 0 12px;
    font-size: 7px; line-height: 15px; letter-spacing: .3px;
    color: var(--grey-text); text-transform: uppercase;
    white-space: nowrap;
  }
  .services-col:first-child { text-align: right; border-right: 1px solid var(--red); }
  .tartan-band {
    position: absolute; left: 0; right: 0; bottom: 0; height: 16px;
    background: linear-gradient(90deg, var(--red-dark), var(--red), var(--red-deep), var(--red), var(--red-dark));
  }
</style>
</head>
<body>
  <section class="card card--front" aria-label="Card front">
    <div class="tartan-field" role="img" aria-label="Red, black and white hatched tartan plaid pattern"></div>
    <div class="front-brand">
      <span class="brand-dot"></span>
      <p class="brand-name">BRIGHTSTONE<br>ROOFING CO.</p>
    </div>
  </section>

  <section class="card card--back" aria-label="Card back">
    <div class="back-brand">
      <span class="brand-dot"></span>
      <p class="brand-name">BRIGHTSTONE<br>ROOFING CO.</p>
    </div>

    <div class="contact-row">
      <div class="person">
        <p class="person-name">EVAN <span class="accent">HART</span></p>
        <p class="person-role">Owner</p>
      </div>
      <span class="divider"></span>
      <ul class="contact-list">
        <li><svg viewBox="0 0 12 12"><path d="M2.5 0.5l2 2.5-1.2 1.4c.7 1.5 1.9 2.7 3.4 3.4L8 6.6l2.5 2-1.2 2.7C4.7 11 1 7.3.5 2.7z"/></svg>555-014-2290</li>
        <li><svg viewBox="0 0 12 12"><path d="M0 2h12v8H0zM1 3v.4l5 3.2 5-3.2V3z"/></svg>evan@brightstoneroofing.co</li>
        <li><svg viewBox="0 0 12 12"><path d="M6 0a6 6 0 100 12A6 6 0 006 0zm0 1.2c.8.8 1.4 2.1 1.6 3.6H4.4C4.6 3.3 5.2 2 6 1.2zM1.3 6.6h2.9c.1 1.6.7 3 1.5 4.1A4.8 4.8 0 011.3 6.6zm0-1.2a4.8 4.8 0 014.4-4.1C4.9 2.4 4.3 3.8 4.2 5.4zm6.5 1.2h2.9a4.8 4.8 0 01-4.4 4.1c.8-1.1 1.4-2.5 1.5-4.1zm0-1.2c-.1-1.6-.7-3-1.5-4.1a4.8 4.8 0 014.4 4.1zM4.4 6.6h3.2C7.4 8.1 6.8 9.4 6 10.2 5.2 9.4 4.6 8.1 4.4 6.6z"/></svg>www.brightstoneroofing.co</li>
      </ul>
    </div>

    <div class="services">
      <ul class="services-col">
        <li>Residential &amp; Commercial Roofing</li>
        <li>Storm Damage &amp; Insurance Claims Specialist</li>
        <li>Fencing. Windows. Gutters. Siding. Sheetrock. Painting</li>
      </ul>
      <ul class="services-col">
        <li>Roof Repairs &amp; Maintenance</li>
        <li>Christmas Lights and Permanent Christmas Light</li>
      </ul>
    </div>

    <div class="tartan-band" role="img" aria-label="Narrow strip of red tartan plaid pattern"></div>
  </section>
</body>
</html>
```